Etikettendesign für Imkereiprodukt
Zielgruppe
Ich betreibe eine Imkerei nach ökologischen Gesichtspunkten und vertreibe alles rund um die Biene- Honig, Wachs, Met, Likör...
Aus Bienenwachs und reinem Leinöl stelle ich ein natürliches Holzwachs her. (Wachs stammt aus eigener Bio Imkerei, Leinöl wird in Deutschland hergestellt)
Mit dem Wachs werden unbehandelte Hölzer imprägniert, gegen Feuchtigkeit geschützt, das Wachs verleiht dem Holz einen matten Glanz
Für dieses Produkt benötige ich ein Etikett.
Aufgabenstellung
- rundes Etikett Durchmesser 85 mm
- Verwendung von eigenem Firmenlogo (Anhang) (Name der Imkerei auch 'Wabenritter')
- Verwendung von folgenden Textbausteinen:
'ausschließlich Leinöl und Bienenwachs'
'regional von Hand hergestellt'
'komplett ohne Lösungsmittel'
oder ähnlich
- Herstelleradresse
- Datei nach Druck-vorgaben

```html
<!DOCTYPE html>
<html lang="de">
<head>
<meta charset="utf-8">
<title>Wabenritter Holzwachs – Etikett</title>
<link rel="stylesheet" href="https://fonts.googleapis.com/css2?family=Montserrat:wght@500&family=Alegreya+Sans:wght@500;700&family=Sacramento&display=swap">
<style>
  :root {
    --page-bg: #ffffff;
    --label-bg: #f7f4ec;
    --band-wood: #c49b63;
    --gold: #b48a4b;
    --ink-navy: #1d3862;
    --band-text: #fbf8f1;
  }
  * { margin: 0; padding: 0; box-sizing: border-box; }
  html, body {
    width: 1088px;
    height: 1200px;
    overflow: hidden;
    background: var(--page-bg);
  }
  .label-stage {
    position: relative;
    width: 1088px;
    height: 1200px;
  }
  .round-label {
    position: absolute;
    left: 0;
    top: 0;
    width: 1088px;
    height: 1200px;
    filter: drop-shadow(0 10px 28px rgba(0, 0, 0, 0.12));
  }
  .label-disc { fill: var(--label-bg); }
  .label-band { fill: var(--band-wood); }
  .brand-mark { fill: none; stroke: var(--gold); stroke-width: 6; }
  .brand-name {
    font-family: "Alegreya Sans", sans-serif;
    font-weight: 700;
    font-size: 44px;
    fill: var(--gold);
  }
  .product-title {
    font-family: "Montserrat", sans-serif;
    font-weight: 500;
    font-size: 104px;
    fill: var(--band-text);
    letter-spacing: 1px;
  }
  .product-subtitle {
    font-family: "Alegreya Sans", sans-serif;
    font-weight: 500;
    font-size: 33px;
    fill: var(--band-text);
    letter-spacing: 0.5px;
  }
  .origin-line {
    font-family: "Sacramento", cursive;
    font-size: 74px;
    fill: var(--ink-navy);
  }
  .rim-claims {
    font-family: "Alegreya Sans", sans-serif;
    font-weight: 500;
    font-size: 32px;
    fill: var(--gold);
    letter-spacing: 0.6px;
  }
</style>
</head>
<body>
<main class="label-stage">
  <svg class="round-label" viewBox="0 0 1088 1200" width="1088" height="1200" aria-label="Rundes Etikett Wabenritter Holzwachs">
    <defs>
      <clipPath id="disc-clip">
        <circle cx="544" cy="600" r="450"/>
      </clipPath>
      <path id="rim-arc" d="M 140.3 708.2 A 418 418 0 0 0 947.7 708.2"/>
    </defs>

    <circle class="label-disc" cx="544" cy="600" r="450"/>

    <g class="label-brand">
      <circle class="brand-mark" cx="544" cy="295" r="78"/>
      <text class="brand-name" x="544" y="440" text-anchor="middle">Wabenritter</text>
    </g>

    <rect class="label-band" x="0" y="508" width="1088" height="190" clip-path="url(#disc-clip)"/>
    <text class="product-title" x="544" y="622" text-anchor="middle">HOLZWACHS</text>
    <text class="product-subtitle" x="544" y="670" text-anchor="middle">Hergestellt aus Leinöl &amp; Bienenwachs</text>

    <text class="origin-line" x="556" y="800" text-anchor="middle" transform="rotate(-5 556 780)">aus dem Havelland</text>

    <text class="rim-claims">
      <textPath href="#rim-arc" startOffset="50%" text-anchor="middle">Komplett ohne Lösungsmittel • Regional von Hand hergestellt</textPath>
    </text>
  </svg>
</main>
</body>
</html>
```